Photography and Political Commentary Blog

Hi there!
I'd like to build a clean, simple, yet visually appealing blog using a theme similar to this: http://www.brightlayouts.net/preview/?layout=CalmForm. I’m looking to work with a designer who has a modern aesthetic who can work with me to create a great blog. Hopefully that’s you!
Details:
The aim would be for the blog to be simple and clean, with each post represented by a picture, title and short summary as with ‘Calm Form’ theme. These post summaries would be displayed in a single area without sidebars or columns.
There would be a home page in addition to four pages that you can access from a menu panel. These subordinate pages would be very similar if not the same in style to the main page. The subordinate pages would be:
- Politics
- Security
- Photography
- Music
For each page:
Politics and Security. These pages would be in a traditional blog format with the ability to post, hyperlink, comment etc. Posts would typically be 200-400 words. I am in the military and actively involved in politics and would like to be able to post my thoughts on issues ‘Quick Thoughts on Big Ideas’, and hyperlink to articles with short personal comments.
Photography. The photography main page would be like the homepage with each post represented by a single photo, title and summary (as per ‘Calm Form’ theme). The individual posts would need to be able to display photo galleries in a grid, with the ability to click on individual photos to view them in high definition. I am open to the use of different widgets to best display the photos. Typically, each gallery would have 6-10 photos. I am a keen amateur (semi-professional?) photographer. This page would showcase small galleries of my artistic work as opposed to large journal/travel style galleries.
Music. This page is a simply way for me to post links to songs I like from ClipRiver, Flickto, Tunepond etc.
I like the clean style and typeface of the following blogs:
http://www.marlow.com/
http://www.nightquay.com/
http://velmorani.com/
http://hattyaboutstuff.com/
http://whichshoesmysonpicked.plumpage.com/
I like color palates similar to these –
http://www.tintfolk.com/swatch/482137/Reed_Heron
http://www.tintfolk.com/swatch/2908/Amber_Nine
The first file I have attached is a logo that uses the types of colors and look I'd like to achieve. The second file I have attached has the type of font I'd like to use (something in the 'Sans' family: http://www.letterbarn.com/fonts/category/sans/
In general, I like the use of red highlights with other neutral tones (greys, blues etc) but I’m open to your ideas!
For the function of the blog, the homepage would be a sequential summary of the posts from each of the subsections (politics, security, photography and music). I'd like this to be grouped so you can see 3 or 4 of the most recent posts from each section - but I'm open to ideas. The main pages for each subsection would be the same: a sequential summary of the posts for that area. If using Postmill, I would like to be able to do this automatically, for instance by allocating ‘categories’ to each post that sort the posts into their respective sections.
The site name will be dermotfarley.com.au. Any logos or headings would be my name ‘Dermot Farley’. I already own the domain name.
The main aim for this project is for it to be clean, simple and elegant (in a modern way). Something that people can open and easily navigate without clutter, yet is visually appealing.
Thanks for taking the time to read this brief and really looking forward to working with you!
Cheers!
Derm

```html
<!DOCTYPE html>
<html lang="en">
<head>
<meta charset="utf-8">
<title>Dermot Farley</title>
<link rel="stylesheet" href="https://fonts.googleapis.com/css2?family=Montserrat:wght@500;600&family=Oswald:wght@400&family=Arimo:wght@400&display=swap">
<style>
  :root {
    --teal-top: #05a5b6;
    --teal-bottom: #067f8e;
    --gold: #edc553;
    --paper: #e4e0db;
    --card: #ffffff;
    --photo: #bab1ac;
    --caption: #1196a6;
    --heading: #d1343f;
    --body-text: #333333;
    --footer: #3b3b3b;
    --footer-text: #d6d6d6;
    --icon-ring: #7a7a7a;
  }
  * { box-sizing: border-box; margin: 0; padding: 0; }
  html, body { width: 1200px; height: 978px; overflow: hidden; }
  body {
    position: relative;
    background: var(--paper);
    font-family: "Arimo", Arial, sans-serif;
  }
  .site-header {
    position: absolute; left: 0; top: 0; width: 1200px; height: 116px;
    background: linear-gradient(to bottom, var(--teal-top), var(--teal-bottom));
    border-bottom: 5px solid var(--gold);
  }
  .site-title {
    position: absolute; left: 107px; top: 32px;
    font-family: "Montserrat", sans-serif; font-weight: 600;
    font-size: 36px; color: #ffffff; letter-spacing: 0.5px;
  }
  .main-nav {
    position: absolute; left: 640px; top: 40px;
    display: flex; gap: 17px;
  }
  .main-nav a {
    font-family: "Oswald", sans-serif; font-weight: 400;
    font-size: 22px; line-height: 1; color: #ffffff;
    text-decoration: none; text-transform: uppercase; letter-spacing: 0.2px;
  }
  .post-card {
    position: absolute; background: var(--card);
    padding: 13px; overflow: hidden;
  }
  .post-photo {
    display: block; width: 100%; height: 125px; background: var(--photo);
  }
  .post-caption {
    margin: 17px 0 0 10px;
    font-family: "Montserrat", sans-serif; font-weight: 500;
    font-size: 14px; color: var(--caption); letter-spacing: 0.6px;
  }
  .post-heading {
    margin: 13px 0 0 10px;
    font-family: "Montserrat", sans-serif; font-weight: 500;
    font-size: 23px; line-height: 1; color: var(--heading);
  }
  .post-summary {
    margin: 8px 0 0 12px; padding-right: 4px;
    font-size: 12.5px; line-height: 21.3px; color: var(--body-text);
    overflow: hidden;
  }
  .lines-5 { height: 107px; }
  .lines-3 { height: 64px; }
  .site-footer {
    position: absolute; left: 0; top: 893px; width: 1200px; height: 85px;
    background: var(--footer);
  }
  .footer-links {
    position: absolute; left: 118px; top: 14px;
    display: flex; gap: 11px;
    font-size: 11px; color: var(--footer-text);
  }
  .footer-links a { color: var(--footer-text); text-decoration: none; }
  .social-links {
    position: absolute; left: 1019px; top: 14px; display: flex; gap: 2px;
  }
</style>
</head>
<body>
  <header class="site-header">
    <div class="site-title">Dermot Farley</div>
    <nav class="main-nav">
      <a href="#">Politics</a>
      <a href="#">Security</a>
      <a href="#">Photography</a>
      <a href="#">Music</a>
    </nav>
  </header>

  <main>
    <article class="post-card" style="left:69px; top:153px; width:412px; height:346px;">
      <div class="post-photo" role="img" aria-label="Post photograph"></div>
      <p class="post-caption">image caption</p>
      <h2 class="post-heading">Heading</h2>
      <p class="post-summary lines-5">Lorem ipsum dolor sit amet, consectetur adipisicing elit, sed do eiusmod tempor incididunt ut labore et dolore magna aliqua. Ut enim ad minim veniam, quis nostrud exercitation ullamco laboris nisi ut aliquip ex ea commodo consequat. Duis aute irure dolor in reprehenderit in voluptate velit esse cillum dolore eu fugiat nulla pariatur.</p>
    </article>

    <article class="post-card" style="left:500px; top:153px; width:280px; height:346px;">
      <div class="post-photo" role="img" aria-label="Post photograph"></div>
      <p class="post-caption">image caption</p>
      <h2 class="post-heading">Heading</h2>
      <p class="post-summary lines-5">Lorem ipsum dolor sit amet, consectetur adipisicing elit, sed do eiusmod tempor incididunt ut labore et dolore magna aliqua. Ut enim ad minim veniam, quis nostrud exercitation ullamco laboris nisi ut aliquip ex ea commodo consequat.</p>
    </article>

    <article class="post-card" style="left:794px; top:158px; width:332px; height:300px;">
      <div class="post-photo" role="img" aria-label="Post photograph"></div>
      <p class="post-caption">image caption</p>
      <h2 class="post-heading">Heading</h2>
      <p class="post-summary lines-3">Lorem ipsum dolor sit amet, consectetur adipisicing elit, sed do eiusmod tempor incididunt ut labore et dolore magna aliqua. Ut enim ad minim veniam, quis nostrud exercitation.</p>
    </article>

    <article class="post-card" style="left:69px; top:516px; width:332px; height:299px;">
      <div class="post-photo" role="img" aria-label="Post photograph"></div>
      <p class="post-caption">image caption</p>
      <h2 class="post-heading">Heading</h2>
      <p class="post-summary lines-3">Lorem ipsum dolor sit amet, consectetur adipisicing elit, sed do eiusmod tempor incididunt ut labore et dolore magna aliqua. Ut enim ad minim veniam, quis nostrud exercitation.</p>
    </article>

    <article class="post-card" style="left:420px; top:516px; width:412px; height:345px;">
      <div class="post-photo" role="img" aria-label="Post photograph"></div>
      <p class="post-caption">image caption</p>
      <h2 class="post-heading">Heading</h2>
      <p class="post-summary lines-5">Lorem ipsum dolor sit amet, consectetur adipisicing elit, sed do eiusmod tempor incididunt ut labore et dolore magna aliqua. Ut enim ad minim veniam, quis nostrud exercitation ullamco laboris nisi ut aliquip ex ea commodo consequat. Duis aute irure dolor in reprehenderit in voluptate velit esse cillum dolore eu fugiat nulla pariatur.</p>
    </article>

    <article class="post-card" style="left:852px; top:515px; width:280px; height:346px;">
      <div class="post-photo" role="img" aria-label="Post photograph"></div>
      <p class="post-caption">image caption</p>
      <h2 class="post-heading">Heading</h2>
      <p class="post-summary lines-5">Lorem ipsum dolor sit amet, consectetur adipisicing elit, sed do eiusmod tempor incididunt ut labore et dolore magna aliqua. Ut enim ad minim veniam, quis nostrud exercitation ullamco laboris nisi ut aliquip ex ea commodo consequat.</p>
    </article>
  </main>

  <footer class="site-footer">
    <div class="footer-links">
      <span>© Dermot Farley. All rights reserved.</span>
      <a href="#">Privacy Policy</a>
      <a href="#">Terms &amp; Conditions</a>
    </div>
    <div class="social-links">
      <svg width="39" height="39" viewBox="0 0 39 39" role="img" aria-label="Social profile link">
        <circle cx="19.5" cy="19.5" r="18" fill="none" stroke="var(--icon-ring)" stroke-width="2"/>
      </svg>
      <svg width="39" height="39" viewBox="0 0 39 39" role="img" aria-label="Social profile link">
        <circle cx="19.5" cy="19.5" r="18" fill="none" stroke="var(--icon-ring)" stroke-width="2"/>
      </svg>
    </div>
  </footer>
</body>
</html>
```